Law Office Business Card

We need a business card design to include the following information:
Name of Firm: Brennick Law Group, P.A.
Address: 4627 Sandlot Ave, Ste 208, West Palm Beach, FL 33409
Phone: 561-555-0148
Fax: 561-555-0193
Website: http://www.tbrennicklaw.example

We Need a place for the Person's name and email address. Please start with the following:
Lorna K. Dwyer, Esq.
lorna@tbrennicklaw.example

```html
<!DOCTYPE html>
<html lang="en">
<head>
<meta charset="utf-8">
<title>Brennick Law Group — Business Card</title>
<link href="https://fonts.googleapis.com/css2?family=EB+Garamond:wght@400;500;600&display=swap" rel="stylesheet">
<style>
  :root {
    --stage: #2b2b2b;
    --paper: #f1f0ee;
    --taupe: #6b5d4f;
    --taupe-dark: #5a4d40;
    --taupe-light: #a89985;
    --ink-logo: #7a6c5c;
    --rule: #b9b4ad;
    --white: #ffffff;
  }
  * { margin: 0; padding: 0; box-sizing: border-box; }
  html, body {
    width: 1200px; height: 840px; overflow: hidden;
    background: var(--stage);
    font-family: "EB Garamond", "Palatino Linotype", serif;
  }
  .canvas { position: relative; width: 1200px; height: 840px; }

  .card { position: absolute; width: 459px; height: 262px; overflow: hidden; }

  /* Front */
  .card--front { left: 452px; top: 121px; background: var(--paper); }
  .front__brand {
    position: absolute; left: 0; top: 0; width: 100%; height: 157px;
    display: flex; flex-direction: column; align-items: center; justify-content: center;
    padding-top: 14px;
  }
  .brand-mark {
    width: 34px; height: 34px; border: 1.5px solid var(--ink-logo); margin-bottom: 10px;
  }
  .brand-name {
    color: var(--ink-logo); font-size: 25px; font-weight: 400; letter-spacing: 0.5px;
    text-transform: uppercase; line-height: 1;
  }
  .brand-sub {
    display: flex; align-items: center; gap: 6px; margin-top: 4px;
    color: var(--ink-logo); font-size: 9px; letter-spacing: 5px; text-transform: uppercase;
  }
  .brand-sub::before, .brand-sub::after {
    content: ""; width: 22px; height: 1px; background: var(--ink-logo);
  }
  .front__band {
    position: absolute; left: 0; top: 157px; width: 100%; height: 105px;
    border-top: 3px solid var(--rule);
    background: radial-gradient(ellipse at 55% 70%, var(--taupe-light) 0%, var(--taupe) 55%, var(--taupe-dark) 100%);
    color: var(--white); padding: 10px 22px 0;
  }
  .band-title {
    display: flex; align-items: center; gap: 8px;
    font-size: 15.5px; letter-spacing: 1px; text-transform: uppercase; white-space: nowrap;
  }
  .band-title::before, .band-title::after {
    content: ""; flex: 1; height: 1px; background: rgba(255,255,255,0.6);
  }
  .band-details {
    display: flex; justify-content: space-between; margin-top: 6px;
    font-size: 13.5px; line-height: 17px;
  }
  .band-details strong { font-weight: 600; }
  .address { text-align: right; }

  /* Back */
  .card--back {
    left: 318px; top: 442px;
    background: radial-gradient(ellipse at 50% 45%, #a3937f 0%, #7d6e5e 45%, #5e5144 100%);
    display: flex; flex-direction: column; align-items: center;
  }
  .back__brand {
    margin-top: 62px; display: flex; align-items: center; gap: 12px; color: var(--white);
  }
  .back__brand .brand-mark { border-color: var(--white); margin: 0; width: 40px; height: 40px; }
  .back__brand .brand-name { color: var(--white); font-size: 30px; }
  .back__person {
    margin-top: 22px; text-align: center; color: var(--white); line-height: 1.3;
  }
  .person-name { font-size: 16px; letter-spacing: 1px; }
  .person-email { font-size: 13px; letter-spacing: 0.5px; }
  .back__url {
    position: absolute; bottom: 24px; width: 100%; text-align: center;
    color: var(--white); font-size: 13px; letter-spacing: 3px;
  }
</style>
</head>
<body>
<main class="canvas">
  <section class="card card--front" aria-label="Business card front">
    <div class="front__brand">
      <div class="brand-mark"></div>
      <div class="brand-name">Brennick Law</div>
      <div class="brand-sub">Group</div>
    </div>
    <div class="front__band">
      <div class="band-title">Brennick Law Group, P.A.</div>
      <div class="band-details">
        <div class="contact">
          <div><strong>P :</strong> 561-555-0148</div>
          <div><strong>F :</strong> 561-555-0193</div>
          <div>www.tbrennicklaw.example</div>
        </div>
        <div class="address">
          <div>4627 Sandlot Ave</div>
          <div>Ste 208</div>
          <div>West Palm Beach, FL 33409</div>
        </div>
      </div>
    </div>
  </section>

  <section class="card card--back" aria-label="Business card back">
    <div class="back__brand">
      <div class="brand-mark"></div>
      <div class="brand-name">Brennick Law</div>
    </div>
    <div class="back__person">
      <div class="person-name">Lorna K. Dwyer, Esq.</div>
      <div class="person-email">lorna@tbrennicklaw.example</div>
    </div>
    <div class="back__url">www.tbrennicklaw.example</div>
  </section>
</main>
</body>
</html>
```